Junk Removal - Customers that are moving

junk collection business we want to gear this mailing to people who are moving and may need help in cleaning out the house for the open house or when the final move is near. Want to sound helpful and show it easier for us to do all the work

Target Market(s)

People Moving

Industry/Entity Type

House

Colors
3277b5
33a6d7

Requirements
Must have
• See attachment

```html
<!DOCTYPE html>
<html lang="en">
<head>
<meta charset="utf-8">
<title>1-800-HAULPRO Moving Postcard</title>
<link rel="stylesheet" href="https://fonts.googleapis.com/css2?family=Anton&family=Roboto+Slab:wght@700;800&family=Open+Sans:wght@700;800&family=PT+Sans+Narrow:wght@400;700&display=swap">
<style>
  :root {
    --brand-blue: #3277b5;
    --sky-blue: #33a6d7;
    --sun-yellow: #fff200;
    --alert-red: #e31e24;
    --ink-navy: #1b1f4a;
    --ink-black: #111111;
    --paper: #ffffff;
    --stage: #efe6d6;
    --rule-grey: #b9b9b9;
    --offer-yellow: #ffe600;
  }
  * { box-sizing: border-box; margin: 0; padding: 0; }
  html, body { width: 1200px; height: 554px; overflow: hidden; }
  body { background: var(--stage); position: relative; font-family: "Open Sans", sans-serif; }

  .card { position: absolute; top: 68px; width: 517px; height: 401px; overflow: hidden; box-shadow: 0 2px 6px rgba(0,0,0,.25); }
  .card--front { left: 52px; background: var(--sun-yellow); }
  .card--back { left: 618px; background: var(--paper); }

  /* Front */
  .front-headline { position: absolute; top: 16px; left: 0; width: 100%; text-align: center; font-family: "Anton", sans-serif; font-weight: 400; font-size: 25px; letter-spacing: .3px; color: var(--ink-black); }
  .front-headline__accent { color: var(--alert-red); }
  .front-panel { position: absolute; left: 0; top: 52px; width: 100%; height: 300px; }
  .service-list { position: absolute; left: 45px; top: 82px; list-style: none; font-family: "Roboto Slab", serif; font-weight: 800; font-size: 16px; line-height: 19.2px; color: var(--ink-navy); }
  .service-list li { padding-left: 17px; position: relative; white-space: nowrap; }
  .service-list li::before { content: ""; position: absolute; left: 0; top: 5px; width: 10px; height: 10px; background: var(--sun-yellow); }
  .service-list li.service-list__more::before { display: none; }
  .brand-name { position: absolute; left: 180px; top: 92px; font-family: "Open Sans", sans-serif; font-weight: 800; font-size: 33px; color: var(--ink-navy); letter-spacing: -.5px; }
  .brand-dot { position: absolute; left: 450px; top: 94px; width: 36px; height: 36px; border-radius: 50%; background: var(--paper); }
  .recycle-art { position: absolute; left: 288px; top: 152px; width: 72px; height: 66px; background: linear-gradient(135deg, #2e9a3f, #1f7a2e); border-radius: 6px; }
  .junk-photo { position: absolute; left: 196px; top: 230px; width: 300px; height: 114px; background: linear-gradient(180deg, #9a8a78 0%, #6e5440 55%, #4a3526 100%); border-radius: 4px; }
  .price-burst { position: absolute; left: 368px; top: 162px; width: 124px; height: 124px; }
  .price-burst__text { position: absolute; inset: 0; display: flex; align-items: center; justify-content: center; text-align: center; font-family: "Open Sans", sans-serif; font-weight: 800; font-size: 12.5px; line-height: 14px; color: var(--paper); }
  .offer { position: absolute; left: 44px; top: 280px; width: 136px; height: 64px; background: var(--offer-yellow); border: 2px dashed var(--alert-red); text-align: center; padding-top: 2px; overflow: hidden; }
  .offer__amount { font-family: "Anton", sans-serif; font-size: 28px; line-height: 34px; color: var(--alert-red); }
  .offer__amount sup { font-size: 16px; }
  .offer__terms { font-weight: 800; font-size: 10.5px; line-height: 16px; letter-spacing: -.2px; white-space: nowrap; color: var(--ink-black); }
  .front-rule { position: absolute; left: 0; top: 349px; width: 100%; height: 3px; background: var(--ink-black); }
  .front-contact { position: absolute; left: 0; top: 358px; width: 100%; text-align: center; font-weight: 700; font-size: 20px; color: var(--alert-red); display: flex; justify-content: center; align-items: center; gap: 6px; }

  /* Back */
  .message-panel { position: absolute; left: 0; top: 0; width: 259px; height: 330px; background: var(--brand-blue); padding: 16px 10px 0 16px; font-family: "PT Sans Narrow", sans-serif; font-weight: 700; color: var(--paper); }
  .message-panel__intro { font-size: 12.5px; line-height: 13.5px; }
  .message-panel__lead { font-size: 14.5px; line-height: 15px; color: var(--alert-red); margin-top: 9px; }
  .message-panel__how { font-size: 15px; margin-top: 6px; }
  .benefit-list { list-style: none; font-size: 10.2px; line-height: 12.4px; }
  .benefit-list li { padding-left: 8px; position: relative; }
  .benefit-list li::before { content: ""; position: absolute; left: 0; top: 4px; width: 4px; height: 4px; border-radius: 50%; background: var(--alert-red); }
  .message-panel__number { text-align: center; font-size: 12.5px; color: var(--alert-red); margin-top: 3px; line-height: 13px; }
  .message-panel__close { text-align: center; font-size: 13px; line-height: 14px; }
  .call-panel { position: absolute; left: 0; top: 330px; width: 259px; height: 71px; background: var(--sun-yellow); text-align: center; padding-top: 6px; font-weight: 800; }
  .call-panel__title { font-variant: small-caps; font-size: 15px; line-height: 18px; color: var(--ink-navy); }
  .call-panel__line { font-size: 14.5px; line-height: 18px; color: var(--alert-red); }
  .mailer-brand { position: absolute; left: 268px; top: 30px; }
  .mailer-brand__tag { font-size: 6.5px; font-weight: 700; color: #6b6b6b; }
  .mailer-brand__tag b { color: var(--ink-navy); }
  .mailer-brand__name { font-weight: 800; font-size: 21px; color: var(--brand-blue); line-height: 24px; letter-spacing: -.3px; }
  .stamp-box { position: absolute; left: 448px; top: 16px; width: 49px; height: 50px; border: 1px solid var(--rule-grey); }
  .address-lines { position: absolute; left: 285px; top: 176px; width: 218px; }
  .address-lines span { display: block; height: 30px; border-bottom: 1px solid var(--rule-grey); }
  .best-burst { position: absolute; left: 326px; top: 296px; width: 92px; height: 92px; }
  .best-burst__text { position: absolute; inset: 0; display: flex; align-items: center; justify-content: center; text-align: center; font-weight: 800; font-variant: small-caps; font-size: 13px; line-height: 13px; color: var(--brand-blue); }
</style>
</head>
<body>

<section class="card card--front" aria-label="Postcard front">
  <h1 class="front-headline"><span class="front-headline__accent">LOWEST PRICED</span> JUNK REMOVAL SERVICES</h1>

  <svg class="front-panel" viewBox="0 0 517 300" preserveAspectRatio="none" aria-hidden="true">
    <path d="M0 30 Q 260 -4 517 4 L517 300 L0 300 Z" fill="var(--sky-blue)"/>
    <path d="M0 30 Q 260 -4 517 4" fill="none" stroke="var(--ink-navy)" stroke-width="3"/>
  </svg>

  <ul class="service-list">
    <li>Furniture</li>
    <li>Books</li>
    <li>Clothing</li>
    <li>Appliances</li>
    <li>Electronics</li>
    <li>Construction debris</li>
    <li>Carpeting</li>
    <li>Mattresses</li>
    <li>Tires</li>
    <li class="service-list__more">and much more!</li>
  </ul>

  <div class="brand-name">1-800-HAULPRO</div>
  <div class="brand-dot" aria-hidden="true"></div>

  <div class="recycle-art" role="img" aria-label="Green recycling arrows graphic"></div>
  <div class="junk-photo" role="img" aria-label="Photo of a pile of household junk: furniture, books, mattress and boxes"></div>

  <div class="price-burst">
    <svg viewBox="0 0 124 124" width="124" height="124" aria-hidden="true">
      <polygon fill="var(--alert-red)" points="62,2 69,21 82,6 84,27 101,15 97,36 117,30 106,48 122,51 108,62 122,73 106,76 117,94 97,88 101,109 84,97 82,118 69,103 62,122 55,103 42,118 40,97 23,109 27,88 7,94 18,76 2,73 16,62 2,51 18,48 7,30 27,36 23,15 40,27 42,6 55,21"/>
    </svg>
    <div class="price-burst__text">THE PRICE<br>WE QUOTE<br>IS THE PRICE<br>YOU PAY!</div>
  </div>

  <div class="offer">
    <div class="offer__amount"><sup>$</sup>25 OFF</div>
    <div class="offer__terms">any junk removal job!</div>
  </div>

  <div class="front-rule"></div>
  <p class="front-contact">
    <svg width="18" height="18" viewBox="0 0 20 20" aria-hidden="true"><circle cx="10" cy="10" r="8.5" fill="none" stroke="var(--alert-red)" stroke-width="1.6"/><path d="M7 5.5 L8.6 8 L7.8 9.1 Q9 11.4 10.9 12.2 L12 11.4 L14.5 13 L13.6 14.6 Q9.5 14.6 6.6 10.6 Q5.5 8.2 7 5.5 Z" fill="var(--alert-red)"/></svg>
    1-800-555-0142 | www.1800haulpro.com
  </p>
</section>

<section class="card card--back" aria-label="Postcard back">
  <div class="message-panel">
    <p class="message-panel__intro">We know how exciting and stressful moving your family and all your belongings can be.</p>
    <p class="message-panel__lead">Let 1-800-HAULPRO help take some of the stress off your move!</p>
    <p class="message-panel__how">Here’s how:</p>
    <ul class="benefit-list">
      <li>No need to collect and remove unwanted items from the property; just point it out and we can do all the work!</li>
      <li>No storage units or dumpsters to deal with, no physical work to worry about.</li>
      <li>We leave the areas from which we remove your unwanted “junk” broom clean.</li>
      <li>Our up front price is not an estimate, the price we quote is the price you pay!</li>
      <li>We responsibly dispose of or recycle all items we remove.</li>
      <li>We are fully licensed (DEP # 0091234) and insured.</li>
      <li>More than 75 years of family business behind all our work.</li>
      <li>Our services are ideal for both the initial cleanout of your open house or final cleanout days before moving</li>
    </ul>
    <p class="message-panel__number">1-800-HAULPRO (1-800-555-0142)</p>
    <p class="message-panel__close">is the one number to call.</p>
  </div>

  <div class="call-panel">
    <p class="call-panel__title">Call Us Today!</p>
    <p class="call-panel__line">✆ 1-800-555-0142</p>
    <p class="call-panel__line">www.1800haulpro.com</p>
  </div>

  <div class="mailer-brand">
    <p class="mailer-brand__tag">SAFE, SECURE JUNK REMOVAL <b>1-800-555-0142</b></p>
    <p class="mailer-brand__name">1-800-HAULPRO</p>
  </div>

  <div class="stamp-box" aria-label="Postage area"></div>

  <div class="address-lines" aria-label="Address lines">
    <span></span><span></span><span></span><span></span>
  </div>

  <div class="best-burst">
    <svg viewBox="0 0 92 92" width="92" height="92" aria-hidden="true">
      <polygon fill="var(--sun-yellow)" points="46,2 52,16 62,5 64,20 77,12 75,28 90,26 81,38 90,46 81,54 90,66 75,64 77,80 64,72 62,87 52,76 46,90 40,76 30,87 28,72 15,80 17,64 2,66 11,54 2,46 11,38 2,26 17,28 15,12 28,20 30,5 40,16"/>
    </svg>
    <div class="best-burst__text">Best<br>Price In<br>Town</div>
  </div>
</section>

</body>
</html>
```